Catalog for our Gold Coins for high value market

We need someone who makes our catalog or book for the gold coins of Switzerland.
Please use the Word Document. The text and the images are below. Feel free to make a nice design. Also make a nice design as a title.
Please use Adobe Indesign or Illustrator to make the content adjustable for us if needed.

You could also add a "star rating" from 1-4 for some of the coins with an image. I will do the rating later. It should be a rating of how precious the coins are without entering a price.
You could also adjust the title design with the coins.

Please make at least the following pages:
Title
Table of content
Title Page for each Ares (Aargau Page 6, Appenzell Page 6, Basel Page 8 and so on)
Pages with the content (Coins including the description)

Target Market(s)

Gold coins collectors. Usually those people are rich men.

Requirements
Must have
• Modern design
Should not have
• Not too many colors used. It should be modern. But have some class.

```html
<!DOCTYPE html>
<html lang="de">
<head>
<meta charset="utf-8">
<title>Coin Brochure – Aargau</title>
<link rel="stylesheet" href="https://fonts.googleapis.com/css2?family=Inter:wght@800&family=DM+Serif+Display&family=Roboto:wght@400&display=swap">
<style>
  :root {
    --page: #ffffff;
    --ink-brown: #4a2810;
    --accent-red: #9a1b1b;
    --body-grey: #5a5a5a;
    --frame-gold: #e9bb3c;
    --gold-light: #f6dd7a;
    --gold-mid: #e2bf4c;
    --gold-dark: #b98d22;
    --folio: #5b5ba6;
  }
  * { margin: 0; padding: 0; box-sizing: border-box; }
  html, body { width: 911px; height: 1200px; overflow: hidden; background: var(--page); }
  .page { position: relative; width: 911px; height: 1200px; background: var(--page); }

  .region-title {
    position: absolute; left: 96px; top: 108px;
    font-family: "Inter", sans-serif; font-weight: 800;
    font-size: 42px; letter-spacing: -0.5px; color: var(--ink-brown);
  }

  .feature-frame {
    position: absolute; left: 96px; top: 189px; width: 729px; height: 374px;
    border: 1.2px solid var(--frame-gold); border-radius: 13px;
  }

  .coin {
    position: absolute; border-radius: 50%;
    background: radial-gradient(circle at 42% 38%, var(--gold-light) 0%, var(--gold-mid) 55%, var(--gold-dark) 100%);
    box-shadow: inset 0 0 0 4px rgba(185,141,34,0.55);
  }
  .coin--feature-obverse { left: 211px; top: 258px; width: 240px; height: 236px; }
  .coin--feature-reverse { left: 471px; top: 260px; width: 236px; height: 232px; }
  .coin--ducat-obverse  { left: 116px; top: 846px; width: 210px; height: 208px; }
  .coin--ducat-reverse  { left: 350px; top: 846px; width: 212px; height: 208px; }

  .section-heading {
    position: absolute; left: 102px;
    font-family: "DM Serif Display", serif; font-weight: 400;
    font-size: 22.5px; color: var(--accent-red); white-space: nowrap;
  }
  .section-heading--ruler { top: 614px; }
  .section-heading--coin  { top: 758px; }

  .ruler-bio {
    position: absolute; left: 102px; top: 654px; width: 740px;
    font-family: "Roboto", sans-serif; font-size: 14.3px; line-height: 24px;
    color: var(--body-grey);
  }

  .footer-label {
    position: absolute; top: 1143px;
    font-family: "Roboto", sans-serif; font-size: 15px; color: var(--ink-brown);
  }
  .footer-label--title { left: 96px; }
  .footer-label--brand { right: 62px; }
  .folio {
    position: absolute; top: 1147px; left: 452px;
    font-family: "Roboto", sans-serif; font-size: 10px; color: var(--folio);
  }
</style>
</head>
<body>
<main class="page">
  <h1 class="region-title">Aargau</h1>

  <section class="feature-frame" aria-label="Hervorgehobene Münze"></section>
  <div class="coin coin--feature-obverse" role="img" aria-label="Goldmedaille, Vorderseite mit Brustbild des Abtes und Umschrift"></div>
  <div class="coin coin--feature-reverse" role="img" aria-label="Goldmedaille, Rückseite mit Ansicht des Klosters und Wappen"></div>

  <h2 class="section-heading section-heading--ruler">Abt Benedikt von Hohenrain 1686 – 1725</h2>
  <p class="ruler-bio">Benedikt Hohenrain (* 21. März 1641 in Talwil; † 9. Oktober 1725 auf Schloss Ravenegg) war ein Schweizer Benediktinermönch. Von 1686 bis 1703 war er Abt, danach bis zu seinem Tod erster Fürstabt des Klosters Lindenau in den Freien Ämtern (im heutigen Kanton Aargau).</p>

  <h2 class="section-heading section-heading--coin">5 Dukaten (Jahr 1720, KAT 4-27b)</h2>
  <div class="coin coin--ducat-obverse" role="img" aria-label="5 Dukaten 1720, Vorderseite mit Brustbild des Abtes"></div>
  <div class="coin coin--ducat-reverse" role="img" aria-label="5 Dukaten 1720, Rückseite mit gekröntem Wappen"></div>

  <footer>
    <span class="footer-label footer-label--title">COIN BROCHURE</span>
    <span class="folio">3</span>
    <span class="footer-label footer-label--brand">YOUR LOGO</span>
  </footer>
</main>
</body>
</html>
```